Popup Banners - BrightCounsel - Legal Technology

- We need two banners (same style) designed with two different images and different text.

- The details of the printing requirements are attached, along with suggested images.

- The banners should share the same theme as our website www.brightcounsel.com.au

- The first banner would include our logo (attached), use the 'roads join' image (attached) in some way and text: New Opportunities - Where legal services and technology meet.

- The second banner would include our logo (attached), use the 'jigsaw' image (attached) in some way and use text: Legal Technology Strategy, Advice and Capability.

- Details on what are required from the Printer is attached also.

Target Market(s)

Legal Professionals

Industry/Entity Type

Information Technology

Font styles to use
Sans Serif

Requirements
Must have
• Our logo (attached), suggested text and the image mentioned for each.
Nice to have
• Professional and modern look
Should not have
• Cheap looking

```html
<!DOCTYPE html>
<html lang="en">
<head>
<meta charset="utf-8">
<title>BrightCounsel Popup Banners</title>
<link rel="stylesheet" href="https://fonts.googleapis.com/css2?family=Arimo:wght@400;700&family=Oswald:wght@500&display=swap">
<style>
  :root {
    --stage: #000000;
    --charcoal: #5e5753;
    --brand-blue: #5a9fd4;
    --white: #ffffff;
    --navy: #0f2a44;
    --sky: #3d86c6;
    --grass: #5f8a34;
  }
  html, body {
    margin: 0;
    padding: 0;
    width: 999px;
    height: 1200px;
    overflow: hidden;
    background: var(--stage);
  }
  .canvas {
    position: relative;
    width: 999px;
    height: 1200px;
  }
  .banner {
    position: absolute;
    top: 100px;
    width: 422px;
    height: 1040px;
    overflow: hidden;
    background: var(--white);
  }
  .banner--roads { left: 68px; }
  .banner--jigsaw { left: 520px; background: var(--navy); }

  .top-strip {
    position: absolute;
    top: 0; left: 0;
    width: 422px; height: 22px;
  }
  .header {
    position: absolute;
    top: 22px; left: 0;
    width: 422px; height: 108px;
    background: var(--white);
    display: flex;
    align-items: center;
    justify-content: center;
    gap: 16px;
  }
  .brand-mark {
    width: 26px; height: 26px;
    background: var(--brand-blue);
  }
  .brand-name {
    font-family: "Arimo", Arial, sans-serif;
    font-weight: 700;
    font-size: 30px;
    letter-spacing: 4px;
    color: var(--charcoal);
  }
  .header-rule {
    position: absolute;
    top: 130px; left: 0;
    width: 422px; height: 8px;
    background: var(--brand-blue);
  }
  .photo {
    position: absolute;
    left: 0; top: 138px;
    width: 422px;
  }
  .photo--roads {
    height: 902px;
    background: linear-gradient(180deg, #2f78be 0%, #7fb2dc 26%, #8fb76a 34%, #6d9a3f 55%, #587f30 80%, #4e7429 100%);
  }
  .photo--jigsaw {
    height: 730px;
    background: radial-gradient(ellipse at 70% 50%, #cfe6f7 0%, #6e9cc4 22%, #2f5e86 50%, #15375a 80%, #0f2a44 100%);
  }
  .headline {
    position: absolute;
    left: 0; width: 422px;
    margin: 0;
    text-align: center;
    font-family: "Oswald", "Arial Narrow", sans-serif;
    font-weight: 500;
    color: var(--white);
    text-transform: uppercase;
  }
  .headline--roads { top: 176px; font-size: 50px; line-height: 60px; }
  .headline--jigsaw { top: 152px; font-size: 35px; line-height: 50px; letter-spacing: 0.3px; }
  .tagline {
    position: absolute;
    top: 684px; left: 0; width: 422px;
    margin: 0;
    text-align: center;
    font-family: "Arimo", Arial, sans-serif;
    font-weight: 700;
    font-size: 31px;
    line-height: 44px;
    color: var(--white);
  }
  .url-band {
    position: absolute;
    top: 868px; left: 0;
    width: 422px; height: 47px;
    background: var(--brand-blue);
    display: flex;
    align-items: center;
    justify-content: center;
    font-family: "Arimo", Arial, sans-serif;
    font-size: 24px;
    color: var(--white);
  }
</style>
</head>
<body>
<main class="canvas">

  <section class="banner banner--roads">
    <svg class="top-strip" viewBox="0 0 422 22" aria-hidden="true">
      <rect width="422" height="22" fill="var(--charcoal)"/>
      <polygon points="332,0 422,0 422,22 342,22" fill="var(--brand-blue)"/>
    </svg>
    <header class="header">
      <span class="brand-mark"></span>
      <span class="brand-name">BrightCounsel</span>
    </header>
    <div class="header-rule"></div>
    <div class="photo photo--roads" role="img" aria-label="Two gravel roads joining on a grassy hill under a blue sky"></div>
    <h1 class="headline headline--roads">New Opportunities</h1>
    <p class="tagline">Where legal services<br>and technology meet.</p>
    <div class="url-band">www.brightcounsel.com.au</div>
  </section>

  <section class="banner banner--jigsaw">
    <svg class="top-strip" viewBox="0 0 422 22" aria-hidden="true">
      <rect width="422" height="22" fill="var(--charcoal)"/>
      <polygon points="332,0 422,0 422,22 342,22" fill="var(--brand-blue)"/>
    </svg>
    <header class="header">
      <span class="brand-mark"></span>
      <span class="brand-name">BrightCounsel</span>
    </header>
    <div class="header-rule"></div>
    <div class="photo photo--jigsaw" role="img" aria-label="Hand placing a jigsaw piece into a backlit blue puzzle"></div>
    <h1 class="headline headline--jigsaw">Legal Technology Strategy,<br>Advice and Capability</h1>
    <div class="url-band">www.brightcounsel.com.au</div>
  </section>

</main>
</body>
</html>
```